Self-driving car ripple effect infographic

Want help putting together an infographic or picture of the ripple effects of the self-driving car. Want to be able to use during a presentation (ppt). Need some kind of "automation" or slide transitions to show & talk to the various ripples.
I have a hand-drawn sketch of the idea.
I will want / need to be able to make edits, corrections, enhancements, etc. to the final project once it's finished. I'm certain I haven't identified all the ripples yet, and will need to make changes to reflect changing landscape.
Graphic Design
- must be able to tell the story (ripples) to an audience via projected ppt.

```html
<!DOCTYPE html>
<html lang="en">
<head>
<meta charset="utf-8">
<title>The Ripple Effect — Driverless Car</title>
<link rel="stylesheet" href="https://fonts.googleapis.com/css2?family=Source+Sans+3:wght@400;600;700;800&display=swap">
<style>
  :root {
    --paper: #ffffff;
    --ink: #111111;
    --frame: #8c8c8c;
    --shadow: #9a9a9a;
    --ripple: #ececec;
    --core: #29abe2;
    --insurance: #111111;
    --enforcement: #e0262b;
    --taxi: #7b3fa0;
    --v2v: #e0248a;
    --v2i: #7a4b1e;
    --cost: #b08a5a;
    --drivers-ed: #f0d000;
    --policy: #29abe2;
    --efficiency: #e0262b;
    --behaviour: #f7931e;
    --getaway: #009245;
    --sharing: #2e3192;
  }
  html, body {
    margin: 0;
    padding: 0;
    width: 782px;
    height: 1200px;
    overflow: hidden;
    background: var(--paper);
  }
  .canvas { display: block; width: 782px; height: 1200px; }
  .title {
    font: 800 19px "Source Sans 3", sans-serif;
    fill: var(--ink);
    text-anchor: middle;
    letter-spacing: 0.3px;
  }
  .title-rule { stroke: var(--ink); stroke-width: 1.2; }
  .frame { fill: var(--paper); stroke: var(--frame); stroke-width: 0.8; }
  .frame-shadow { fill: none; stroke: var(--shadow); stroke-width: 3; opacity: .5; }
  .ripple { fill: none; stroke: var(--ripple); stroke-width: 12; opacity: .6; }
  .callout { fill: var(--paper); stroke: var(--ink); stroke-width: 0.9; }
  .callout-shadow { fill: var(--shadow); opacity: .7; }
  .callout-text { font: 400 8.3px "Source Sans 3", sans-serif; fill: var(--ink); }
  .callout-text.center { text-anchor: middle; font-size: 8.8px; }
  .callout-text.big { text-anchor: middle; font-size: 9.4px; font-weight: 700; }
  .callout-rule { stroke: var(--ink); stroke-width: 0.6; }
  .pointer { stroke: var(--ink); stroke-width: 1; fill: none; }
  .core { font: 700 9.4px "Source Sans 3", sans-serif; fill: var(--core); text-anchor: middle; }
  .label { font: 400 8.3px "Source Sans 3", sans-serif; text-anchor: middle; }
  .link { stroke-width: 1.5; fill: none; }

  .label.insurance   { fill: var(--t-insurance); }
  .label.enforcement { fill: var(--t-enforcement); }
  .label.taxi        { fill: var(--t-taxi); }
  .label.v2v         { fill: var(--t-v2v); }
  .label.v2i         { fill: var(--t-v2i); }
  .label.cost        { fill: var(--t-cost); }
  .label.drivers-ed  { fill: var(--t-drivers-ed); }
  .label.policy      { fill: var(--t-policy); }
  .label.efficiency  { fill: var(--t-efficiency); }
  .label.behaviour   { fill: var(--t-behaviour); }
  .label.getaway     { fill: var(--t-getaway); }
  .label.sharing     { fill: var(--t-sharing); }

  .link.insurance   { stroke: var(--insurance); }
  .link.enforcement { stroke: var(--enforcement); }
  .link.taxi        { stroke: var(--taxi); }
  .link.v2v         { stroke: var(--v2v); }
  .link.v2i         { stroke: var(--v2i); }
  .link.cost        { stroke: var(--cost); }
  .link.drivers-ed  { stroke: var(--drivers-ed); }
  .link.policy      { stroke: var(--policy); }
  .link.efficiency  { stroke: var(--efficiency); }
  .link.behaviour   { stroke: var(--behaviour); }
  .link.getaway     { stroke: var(--getaway); }
  .link.sharing     { stroke: var(--sharing); }

  .map--mono {
    --t-insurance: var(--ink); --t-enforcement: var(--ink); --t-taxi: var(--ink);
    --t-v2v: var(--ink); --t-v2i: var(--ink); --t-cost: var(--ink);
    --t-drivers-ed: var(--ink); --t-policy: var(--ink); --t-efficiency: var(--ink);
    --t-behaviour: var(--ink); --t-getaway: var(--ink); --t-sharing: var(--ink);
  }
  .map--colour {
    --t-insurance: var(--insurance); --t-enforcement: var(--enforcement); --t-taxi: var(--taxi);
    --t-v2v: var(--v2v); --t-v2i: var(--v2i); --t-cost: var(--cost);
    --t-drivers-ed: var(--drivers-ed); --t-policy: var(--policy); --t-efficiency: var(--efficiency);
    --t-behaviour: var(--behaviour); --t-getaway: var(--getaway); --t-sharing: var(--sharing);
  }
</style>
</head>
<body>
<svg class="canvas" viewBox="0 0 600 920" xmlns="http://www.w3.org/2000/svg" role="img" aria-label="The ripple effect of the driverless car, shown in a monochrome and a colour version">
  <defs>
    <g id="ripple-map">
      <text class="title" x="313" y="66">THE RIPPLE EFFECT</text>
      <line class="title-rule" x1="227" y1="70" x2="399" y2="70"/>

      <rect class="frame-shadow" x="50" y="100" width="523" height="362"/>
      <rect class="frame" x="48" y="98" width="523" height="362"/>

      <circle class="ripple" cx="315" cy="270" r="60"/>
      <circle class="ripple" cx="315" cy="270" r="120"/>
      <circle class="ripple" cx="315" cy="270" r="180"/>

      <!-- stats -->
      <rect class="callout-shadow" x="466" y="44" width="115" height="117"/>
      <rect class="callout" x="463" y="41" width="115" height="117"/>
      <text class="callout-text" x="470" y="54">USA</text>
      <line class="callout-rule" x1="470" y1="56" x2="486" y2="56"/>
      <text class="callout-text" x="470" y="68">&gt;5M accidents</text>
      <text class="callout-text" x="470" y="81">&gt; 9M vehicles</text>
      <text class="callout-text" x="470" y="94">&gt; 32K killed</text>
      <text class="callout-text" x="470" y="117">Lost Productivity $300B</text>
      <text class="callout-text" x="470" y="130">$450B in costs per year</text>
      <text class="callout-text" x="470" y="143">(med, prop, legal...)</text>

      <!-- premium reduction -->
      <rect class="callout-shadow" x="69" y="95" width="92" height="32"/>
      <rect class="callout" x="66" y="92" width="92" height="32"/>
      <text class="callout-text center" x="112" y="105">~ 75% reduction</text>
      <text class="callout-text center" x="112" y="117">($200B today)</text>
      <line class="pointer" x1="122" y1="124" x2="122" y2="150"/>

      <!-- parking -->
      <rect class="callout-shadow" x="511" y="406" width="67" height="55"/>
      <rect class="callout" x="508" y="403" width="67" height="55"/>
      <text class="callout-text big" x="541" y="415">2B</text>
      <text class="callout-text big" x="541" y="427">Parking</text>
      <text class="callout-text big" x="541" y="439">Spots</text>
      <text class="callout-text big" x="541" y="451">today</text>
      <line class="pointer" x1="466" y1="440" x2="508" y2="428"/>
      <line class="pointer" x1="466" y1="445" x2="508" y2="446"/>

      <g class="links">
        <line class="link insurance" x1="298" y1="258" x2="280" y2="210"/>
        <line class="link insurance" x1="258" y1="199" x2="236" y2="186"/>
        <line class="link insurance" x1="189" y1="178" x2="171" y2="163"/>
        <line class="link insurance" x1="256" y1="172" x2="264" y2="186"/>
        <line class="link insurance" x1="244" y1="126" x2="249" y2="146"/>
        <line class="link insurance" x1="258" y1="206" x2="226" y2="213"/>
        <line class="link insurance" x1="145" y1="161" x2="124" y2="179"/>
        <line class="link insurance" x1="108" y1="150" x2="138" y2="150"/>

        <line class="link enforcement" x1="327" y1="262" x2="356" y2="209"/>
        <line class="link enforcement" x1="359" y1="166" x2="359" y2="186"/>
        <line class="link enforcement" x1="375" y1="196" x2="410" y2="182"/>
        <line class="link enforcement" x1="375" y1="201" x2="409" y2="201"/>
        <line class="link enforcement" x1="446" y1="201" x2="481" y2="199"/>

        <line class="link taxi" x1="315" y1="227" x2="315" y2="258"/>
        <line class="link v2v" x1="266" y1="245" x2="292" y2="262"/>
        <line class="link v2i" x1="331" y1="262" x2="352" y2="248"/>

        <line class="link cost" x1="342" y1="270" x2="388" y2="266"/>
        <line class="link cost" x1="430" y1="266" x2="464" y2="268"/>

        <line class="link drivers-ed" x1="334" y1="277" x2="365" y2="292"/>

        <line class="link policy" x1="99" y1="272" x2="128" y2="272"/>
        <line class="link policy" x1="178" y1="272" x2="206" y2="272"/>
        <line class="link policy" x1="250" y1="271" x2="286" y2="271"/>

        <line class="link efficiency" x1="298" y1="282" x2="281" y2="295"/>
        <line class="link efficiency" x1="228" y1="307" x2="212" y2="315"/>
        <line class="link efficiency" x1="170" y1="341" x2="136" y2="358"/>

        <line class="link behaviour" x1="305" y1="282" x2="279" y2="334"/>
        <line class="link behaviour" x1="262" y1="369" x2="257" y2="387"/>
        <line class="link behaviour" x1="227" y1="393" x2="206" y2="392"/>
        <line class="link behaviour" x1="232" y1="399" x2="206" y2="416"/>
        <line class="link behaviour" x1="242" y1="400" x2="239" y2="415"/>

        <line class="link getaway" x1="315" y1="282" x2="315" y2="338"/>
        <line class="link getaway" x1="315" y1="373" x2="315" y2="386"/>

        <line class="link sharing" x1="322" y1="282" x2="360" y2="334"/>
        <line class="link sharing" x1="387" y1="348" x2="416" y2="347"/>
        <line class="link sharing" x1="369" y1="358" x2="369" y2="373"/>
        <line class="link sharing" x1="360" y1="396" x2="344" y2="430"/>
        <line class="link sharing" x1="377" y1="396" x2="389" y2="412"/>
        <line class="link sharing" x1="386" y1="353" x2="432" y2="389"/>
        <line class="link sharing" x1="454" y1="414" x2="454" y2="436"/>
        <line class="link sharing" x1="443" y1="340" x2="446" y2="313"/>
        <line class="link sharing" x1="460" y1="342" x2="489" y2="318"/>
        <line class="link sharing" x1="460" y1="347" x2="488" y2="343"/>
        <line class="link sharing" x1="456" y1="352" x2="486" y2="368"/>
      </g>

      <g class="labels">
        <text class="core" x="315" y="273">DRIVERLESS CAR</text>

        <text class="label insurance" x="241" y="110">Fewer<tspan x="241" dy="11">Body Shops</tspan></text>
        <text class="label insurance" x="253" y="156">Less Prop<tspan x="253" dy="11">Damage &amp; BI</tspan></text>
        <text class="label insurance" x="158" y="146">Less<tspan x="158" dy="11">premiums</tspan></text>
        <text class="label insurance" x="87" y="146">Shrinking<tspan x="87" dy="11">Market</tspan></text>
        <text class="label insurance" x="112" y="185">New insurers<tspan x="112" dy="11">(Searchly, Oems)</tspan></text>
        <text class="label insurance" x="212" y="183">Lower Rates</text>
        <text class="label insurance" x="269" y="193">Fewer<tspan x="269" dy="11">Crashes</tspan></text>
        <text class="label insurance" x="197" y="213">No Personnal<tspan x="197" dy="11">Injury Lawyers</tspan></text>

        <text class="label taxi" x="315" y="211">No Taxi<tspan x="315" dy="11">Drivers</tspan></text>
        <text class="label v2v" x="260" y="240">V2V industry</text>
        <text class="label v2i" x="369" y="243">V2I industry</text>

        <text class="label enforcement" x="357" y="152">No<tspan x="357" dy="11">Traffic Courts</tspan></text>
        <text class="label enforcement" x="360" y="193">No<tspan x="360" dy="11">Tickets</tspan></text>
        <text class="label enforcement" x="434" y="168">No Revenue<tspan x="434" dy="11">from Violations</tspan></text>
        <text class="label enforcement" x="427" y="202">No Speed<tspan x="427" dy="11">Traps</tspan></text>
        <text class="label enforcement" x="506" y="190">Police<tspan x="506" dy="11">Concentrate</tspan><tspan x="506" dy="11">on other</tspan><tspan x="506" dy="11">Crimes</tspan></text>

        <text class="label cost" x="408" y="262">More<tspan x="408" dy="11">Expensive</tspan><tspan x="408" dy="11">Cars</tspan></text>
        <text class="label cost" x="489" y="265">Tech<tspan x="489" dy="11">Innovation</tspan></text>
        <text class="label drivers-ed" x="378" y="291">No<tspan x="378" dy="11">Drivers</tspan><tspan x="378" dy="11">ed</tspan></text>

        <text class="label policy" x="78" y="267">Extended<tspan x="78" dy="11">warranty</tspan></text>
        <text class="label policy" x="153" y="267">No "at fault"<tspan x="153" dy="11">Accidents</tspan></text>
        <text class="label policy" x="229" y="261">New<tspan x="229" dy="11">Insurance</tspan><tspan x="229" dy="11">policy</tspan></text>

        <text class="label efficiency" x="254" y="298">Improved<tspan x="254" dy="11">Operating</tspan><tspan x="254" dy="11">Efficiency</tspan></text>
        <text class="label efficiency" x="188" y="320">Increased<tspan x="188" dy="11">Fuel</tspan><tspan x="188" dy="11">Efficiency</tspan></text>
        <text class="label efficiency" x="117" y="362">Oil Prices<tspan x="117" dy="11">Fall</tspan></text>

        <text class="label behaviour" x="266" y="343">In-car<tspan x="266" dy="11">Behavior</tspan><tspan x="266" dy="11">Changes</tspan></text>
        <text class="label behaviour" x="243" y="396">Platform</text>
        <text class="label behaviour" x="180" y="387">Mobile<tspan x="180" dy="11">Hot Spots</tspan></text>
        <text class="label behaviour" x="196" y="424">TXT</text>
        <text class="label behaviour" x="239" y="426">Apps</text>

        <text class="label getaway" x="315" y="347">No<tspan x="315" dy="11">"get-away"</tspan><tspan x="315" dy="11">Drivers</tspan></text>
        <text class="label getaway" x="315" y="394">Fewer Bank<tspan x="315" dy="11">Robberies</tspan></text>

        <text class="label sharing" x="369" y="343">Car<tspan x="369" dy="11">Sharing</tspan></text>
        <text class="label sharing" x="369" y="382">Increased<tspan x="369" dy="11">Utilization</tspan></text>
        <text class="label sharing" x="337" y="439">Maintenance</text>
        <text class="label sharing" x="395" y="421">"Fleet"<tspan x="395" dy="11">Concierge</tspan><tspan x="395" dy="11">Services</tspan></text>
        <text class="label sharing" x="437" y="349">Fewer Cars</text>
        <text class="label sharing" x="449" y="298">Less<tspan x="449" dy="11">Congestion</tspan></text>
        <text class="label sharing" x="514" y="295">Finance Cos.<tspan x="514" dy="11">(personnal</tspan><tspan x="514" dy="11">auto loans)</tspan></text>
        <text class="label sharing" x="518" y="338">Smaller cars<tspan x="518" dy="11">or "trip specific"</tspan><tspan x="518" dy="11">Vehicles</tspan></text>
        <text class="label sharing" x="501" y="376">Shrinking<tspan x="501" dy="11">Detroit</tspan></text>
        <text class="label sharing" x="456" y="398">No Garage/<tspan x="456" dy="11">Parking Decks</tspan></text>
        <text class="label sharing" x="454" y="446">Depot</text>
      </g>
    </g>
  </defs>

  <use href="#ripple-map" class="map map--mono"/>
  <use href="#ripple-map" class="map map--colour" y="458"/>
</svg>
</body>
</html>
```